Harborstone Lending Business Card Design

We are looking for a nice looking business card design. I'd prefer something other than white for the background but white is ok if necessary. I'm uploading two versions of my picture, one is square and one is rounded. Also a couple of versions of the logo for white backgrounds as well as one for darker backgrounds.

Target Market(s)

Realtors and prospective clients

Industry/Entity Type

Mortgage

Contact Information for Business Card

Double sided business card. Not sure what is needed here.

Colors

Designer to choose colors to be used in the design.

Requirements
Must have
• Name: Marcus Pellham
• Title: Senior Mortgage Advisor
• Email: marcuspellham@harborstonelending.example
• website: www.marcuspellhamhomeloangroup.example
• Address: 4670 W 2850 N, STE 215 Salt Lake City, UT 84192
• Phone: 801-555-0187
• nmls# 948217
• Logo is on our webstie. www.harborstonelending.example
• Picture
Nice to have
• Colors could be similar to our website www.harborstonelending.example
• A list of what we do (VA Loans, FHA Loans, Conventional Loans, USDA Loans)

```html
<!DOCTYPE html>
<html lang="en">
<head>
<meta charset="utf-8">
<title>Harborstone Lending Business Card</title>
<link href="https://fonts.googleapis.com/css2?family=Cinzel:wght@600&family=Didact+Gothic&display=swap" rel="stylesheet">
<style>
  :root {
    --page: #3a3a3a;
    --ink: #1e1e1e;
    --text: #3c3c3c;
    --green: #72a03a;
    --card-white: #ffffff;
    --card-grey-top: #f4f4f4;
    --card-grey-bottom: #dcdcdc;
    --faint: #ececec;
  }
  * { box-sizing: border-box; margin: 0; padding: 0; }
  html, body { width: 1200px; height: 834px; overflow: hidden; }
  body {
    background: var(--page);
    font-family: "Didact Gothic", sans-serif;
    color: var(--text);
    position: relative;
  }
  .card {
    position: absolute;
    width: 540px;
    height: 310px;
    top: 262px;
    box-shadow: 0 10px 30px rgba(0,0,0,.45);
    overflow: hidden;
  }
  .card-front {
    left: 40px;
    background: linear-gradient(160deg, var(--card-grey-top), var(--card-grey-bottom));
  }
  .card-back { left: 620px; background: var(--card-white); }

  .brand {
    position: absolute;
    display: flex;
    align-items: center;
    gap: 10px;
    font-family: "Cinzel", serif;
    font-weight: 600;
    color: var(--ink);
    white-space: nowrap;
  }
  .brand-mark { background: var(--ink); flex: none; }
  .card-front .brand { left: 0; right: 0; top: 100px; justify-content: center; font-size: 30px; letter-spacing: 3px; }
  .card-front .brand-mark { width: 30px; height: 30px; }
  .front-band {
    position: absolute;
    left: 0; right: 0; top: 196px;
    height: 34px;
    background: var(--green);
    color: #fff;
    font-size: 15px;
    letter-spacing: .3px;
    display: flex;
    align-items: center;
    justify-content: center;
  }

  .card-back .brand { right: 28px; top: 30px; font-size: 17px; letter-spacing: 2px; gap: 7px; }
  .card-back .brand-mark { width: 16px; height: 16px; }
  .tribute-art {
    position: absolute;
    right: 0; top: 70px;
    width: 240px; height: 240px;
    background: radial-gradient(ellipse at 65% 55%, #e2e2e2 0%, var(--faint) 45%, rgba(255,255,255,0) 75%);
  }
  .advisor { position: absolute; left: 42px; top: 130px; width: 340px; }
  .advisor-name {
    font-family: "Cinzel", serif;
    font-weight: 600;
    font-size: 21px;
    color: var(--ink);
    letter-spacing: .5px;
  }
  .advisor-title { color: var(--green); font-size: 13px; margin-top: 2px; }
  .advisor-address { font-size: 10.5px; line-height: 1.45; margin-top: 10px; }
  .contact-list { list-style: none; margin-top: 12px; }
  .contact-list li {
    display: flex;
    align-items: center;
    gap: 12px;
    font-size: 12px;
    height: 20px;
    white-space: nowrap;
  }
  .contact-list svg { width: 13px; height: 13px; flex: none; fill: none; stroke: var(--green); stroke-width: 1.8; }
</style>
</head>
<body>
  <section class="card card-front">
    <div class="brand"><span class="brand-mark"></span>Harborstone Lending</div>
    <div class="front-band">www.marcuspellhamhomeloangroup.example</div>
  </section>

  <section class="card card-back">
    <div class="tribute-art" role="img" aria-label="Faint grey illustration of saluting service members beneath stars"></div>
    <div class="brand"><span class="brand-mark"></span>Harborstone Lending</div>
    <div class="advisor">
      <h1 class="advisor-name">Marcus Pellham</h1>
      <p class="advisor-title">Senior Mortgage Advisor</p>
      <p class="advisor-address">4670 W 2850 N, STE 215 Salt<br>Lake City, UT 84192</p>
      <ul class="contact-list">
        <li><svg viewBox="0 0 14 14"><path d="M2 5c0-2 2-3 5-3s5 1 5 3M4 6h6l1 6H3z"/></svg>801-555-0187</li>
        <li><svg viewBox="0 0 14 14"><rect x="1.5" y="3" width="11" height="8"/><path d="M1.5 3l5.5 5 5.5-5"/></svg>marcuspellham@harborstonelending.example</li>
        <li><svg viewBox="0 0 14 14"><circle cx="7" cy="7" r="5.5"/><path d="M1.5 7h11M7 1.5c-3 3-3 8 0 11M7 1.5c3 3 3 8 0 11"/></svg>www.marcuspellhamhomeloangroup.example</li>
        <li><svg viewBox="0 0 14 14"><path d="M5 1.5l-1.5 11M10 1.5l-1.5 11M2 5h10.5M1.5 9.5h10.5"/></svg>nmls : 948217</li>
      </ul>
    </div>
  </section>
</body>
</html>
```